Brightvale Marketing Banner for emails to customers

Hi Marketing Team The information is to be a nice banner say half page on Marketing our Services to prospective customers, this is embedded into an email so something nice with the content that I will provide. Based on a nice background to highlight our service portfolio aligned to our website
www.brightvale-example.com.au

```html
<!DOCTYPE html>
<html lang="en">
<head>
<meta charset="utf-8">
<title>Brightvale Marketing Banner</title>
<link rel="stylesheet" href="https://fonts.googleapis.com/css2?family=Merriweather:wght@300;400;700;900&display=swap">
<style>
  :root{
    --navy:#2a3d6b;
    --orange:#cf4a1c;
    --ink:#3b3b44;
    --lavender:#c4c2d8;
    --page:#ececec;
    --card:#ffffff;
  }
  *{box-sizing:border-box;margin:0;padding:0}
  html,body{width:1200px;height:1200px;overflow:hidden;background:var(--page)}
  body{font-family:"Merriweather",Georgia,serif;color:var(--ink)}
  .banner{position:absolute;left:56px;top:0;width:1088px;height:1200px;overflow:hidden;background:#f7f6f8}
  .banner-backdrop{position:absolute;inset:0;
    background:
      radial-gradient(ellipse 300px 380px at 930px 200px, rgba(214,190,178,.55), transparent 70%),
      radial-gradient(ellipse 500px 420px at 800px 780px, rgba(205,205,215,.45), transparent 70%),
      linear-gradient(100deg,#fbfbfc 0%,#f2f1f3 45%,#e5e2e4 100%);}
  .brand{position:absolute;left:334px;top:145px;display:flex;align-items:center;gap:14px}
  .brand-dot{width:62px;height:62px;border-radius:50%;background:var(--navy)}
  .brand-name{font-size:62px;font-weight:400;color:var(--navy);line-height:1}
  .brand-url{position:absolute;left:432px;top:218px;font-size:23px;color:var(--orange)}
  .intro{position:absolute;left:334px;top:287px;width:720px}
  .intro h1{font-size:32px;font-weight:900;color:var(--navy);line-height:1.2;letter-spacing:-.3px}
  .intro p{font-size:20.5px;font-weight:300;line-height:1.38;margin-top:14px;color:#3a3a42}
  .intro p + p{margin-top:26px}
  .intro strong{font-weight:900;color:var(--navy)}
  .intro-rule{width:66px;height:4px;background:var(--navy);margin-top:24px}
  .photo{position:absolute;top:576px;width:304px;height:178px;border-radius:16px}
  .photo-exterior{left:116px;background:linear-gradient(90deg,#5f7f8f 0%,#6f8aa0 30%,#4b4f55 55%,#5a5c60 100%)}
  .photo-warehouse{left:591px;background:linear-gradient(90deg,#3f5f9e 0%,#7f8aa0 35%,#d7d3c9 60%,#3d3f46 80%,#d9d66a 100%)}
  .card{position:absolute;top:737px;width:425px;height:332px}
  .card::before{content:"";position:absolute;inset:0;background:var(--card);border-radius:28px;transform:skewX(-6deg);box-shadow:0 6px 14px rgba(0,0,0,.08)}
  .card::after{content:"";position:absolute;left:24px;right:52px;bottom:-2px;height:6px;border-radius:4px;transform:skewX(-6deg)}
  .card-services{left:108px}
  .card-services::after{background:var(--orange)}
  .card-upgrades{left:585px}
  .card-upgrades::after{background:var(--navy)}
  .card-body{position:relative;z-index:1;padding:18px 0 0 70px}
  .card-upgrades .card-body{padding:10px 36px 0 63px}
  .card-title{font-size:38px;font-weight:900;line-height:1.08;color:var(--navy)}
  .card-upgrades .card-title{font-size:34px}
  .card-title span{color:var(--orange);display:block}
  .service-list{list-style:none;margin-top:22px;margin-left:-34px}
  .service-list li{position:relative;padding-left:34px;font-size:20px;font-weight:300;line-height:1.3;color:#3a3a42;width:350px}
  .service-list li::before{content:"";position:absolute;left:4px;top:8px;width:12px;height:12px;border-radius:50%;background:var(--lavender)}
  .card-upgrades p{font-size:20px;font-weight:300;line-height:1.3;text-align:justify;color:#3a3a42;margin-top:18px}
  .card-upgrades p + p{margin-top:22px}
  .service-bar{position:absolute;left:0;right:0;top:1101px;height:99px;background:var(--navy);color:#fff;text-align:center;padding-top:12px}
  .service-bar h2{font-size:32px;font-weight:900;letter-spacing:.4px}
  .service-bar p{font-size:18px;font-weight:400;margin-top:2px}
</style>
</head>
<body>
  <main class="banner">
    <div class="banner-backdrop" role="img" aria-label="Soft blurred background photo of a smiling customer service representative"></div>

    <div class="brand">
      <span class="brand-dot"></span>
      <span class="brand-name">Brightvale</span>
    </div>
    <div class="brand-url">www.brightvale-example.com.au</div>

    <section class="intro">
      <h1>Hope you are keeping well during this time.</h1>
      <p><strong>Brightvale</strong> has been in business for 15 years and built a strong and steady market reputation.</p>
      <p>Please find attached our Brightvale Marketing Brochure detailing our dedicated portfolio offerings for your perusal.</p>
      <div class="intro-rule"></div>
    </section>

    <div class="photo photo-exterior" role="img" aria-label="Photo of a worker pressure cleaning a brick wall"></div>
    <div class="photo photo-warehouse" role="img" aria-label="Photo of a team reviewing a tablet in a warehouse"></div>

    <article class="card card-services">
      <div class="card-body">
        <h2 class="card-title"><span>Portfolio</span>of Services:</h2>
        <ul class="service-list">
          <li>Equipment Sundae Machine Cleaning Service.</li>
          <li>Detailed Kitchen Cleaning and Vat Boil Outs</li>
          <li>Gurney High Pressure and Playground Cleaning</li>
          <li>General Facility Maintenance</li>
        </ul>
      </div>
    </article>

    <article class="card card-upgrades">
      <div class="card-body">
        <h2 class="card-title"><span>Business Upgrades</span>completed</h2>
        <p>We have upgraded and digitalised our reporting system for transparency across our services.</p>
        <p>Our Team Members have received ongoing refresher training to keep skills refreshed and Market aligned.</p>
      </div>
    </article>

    <footer class="service-bar">
      <h2>Customer Service:</h2>
      <p>Welcome to call on Customer Service Ph@ 1300 555 010 or Email: service@brightvale-example.com.au for Service.</p>
    </footer>
  </main>
</body>
</html>
```